Coffee Brand Poster Ad

We' re looking for design of poster advertisement for our coffee brand, kind of poster we can put in elevators or buses (approx. size 50x60cm), so we're looking for something original and eye-catchy ideas. We dont have our own specific slogan for this, so feel free to experiment. It is high-quality instant coffee made according to european nordic recipe, our target are women in overall, but mainly young, middle-class modern girls. It is high-quality instant coffee made according to european nordic recipe. Were trying to turn drinking coffee into lifestyle choice for young chinese girls by emphasizing western influence for our brand, also focus on elegance and classy style in packaging and advertisements. Our coffee brand is currently dedicated to sell mainly in China so we prefer english and chinese simplified version. If youre not familiar with chinese language you can use online translator, we will correct or adjust it to our needs.

Target Market(s)

Industry/Entity Type

Requirements
Must have
• - Our brand logo (*cdr and *png file included as attachement)
- Poster size 50x60 cm
- Originality and creative idea
Nice to have
• - Should draw attention and create curiosity at first sight
- It should emphasize 'CLASSY' style of our coffee or lifestyle of young energetic girls
- might compare chinese and western lifestyle
Should not have
• - Don't try to focus on "waking up" aspect of coffee
- Too much coffe beans

```html
<!DOCTYPE html>
<html lang="en">
<head>
<meta charset="utf-8">
<title>When Coffee Become Your Lifestyle — Fjord Grace Poster</title>
<link rel="stylesheet" href="https://fonts.googleapis.com/css2?family=Oswald:wght@500;600&family=Great+Vibes&display=swap">
<style>
  :root {
    --wine: #6d100c;
    --cream: #dcc6a6;
    --ornament-tone: #8c3a2c;
    --illustration-tone: #8a2a20;
  }
  * { margin: 0; padding: 0; box-sizing: border-box; }
  html, body {
    width: 1000px;
    height: 1200px;
    overflow: hidden;
    background: var(--wine);
  }
  .poster {
    position: relative;
    width: 1000px;
    height: 1200px;
    background: var(--wine);
    color: var(--cream);
    font-family: "Oswald", "Arial Narrow", sans-serif;
    font-weight: 600;
    text-transform: uppercase;
  }
  .poster__frame {
    position: absolute;
    inset: 0;
  }
  .headline {
    position: absolute;
    left: 0;
    width: 100%;
    text-align: center;
    line-height: 1;
    white-space: nowrap;
  }
  .headline--when {
    top: 160px;
    font-size: 84px;
    letter-spacing: 68px;
    padding-left: 68px;
  }
  .headline--coffee {
    top: 246px;
    font-size: 172px;
    letter-spacing: -3px;
    transform: scaleX(0.9);
  }
  .headline--become {
    top: 686px;
    font-size: 96px;
    letter-spacing: -1px;
    transform: scaleX(0.88);
  }
  .headline--lifestyle {
    top: 768px;
    font-size: 114px;
    letter-spacing: -1px;
    transform: scaleX(0.9);
  }
  .cup-illustration {
    position: absolute;
    left: 362px;
    top: 410px;
    width: 296px;
    height: 240px;
    border-radius: 50% 50% 46% 46%;
    background: radial-gradient(ellipse at 45% 55%, var(--illustration-tone) 0%, var(--wine) 72%);
  }
  .brand {
    position: absolute;
    left: 0;
    top: 978px;
    width: 100%;
    text-align: center;
    font-family: "Oswald", "Arial Narrow", sans-serif;
    font-weight: 500;
    font-size: 40px;
    letter-spacing: 3px;
    text-transform: none;
    line-height: 1;
  }
</style>
</head>
<body>
  <main class="poster">
    <svg class="poster__frame" width="1000" height="1200" viewBox="0 0 1000 1200" aria-hidden="false">
      <rect class="frame-line frame-line--outer" x="52" y="44" width="896" height="1112" rx="14" fill="none" stroke="var(--cream)" stroke-width="3"/>
      <path class="ornament-band" role="img" aria-label="Scrolling vine ornament running around the border"
            fill="var(--ornament-tone)" fill-rule="evenodd"
            d="M64 56 H936 V1144 H64 Z M136 112 H864 V1088 H136 Z"/>
      <rect class="frame-line frame-line--inner" x="64" y="56" width="872" height="1088" rx="8" fill="none" stroke="var(--cream)" stroke-width="2"/>
    </svg>

    <h1 class="headline headline--when">When</h1>
    <div class="headline headline--coffee">Coffee</div>

    <div class="cup-illustration" role="img" aria-label="Sketched steaming coffee cup on a saucer with a butterfly on the rim and two coffee beans"></div>

    <div class="headline headline--become">Become Your</div>
    <div class="headline headline--lifestyle">Lifestyle</div>

    <div class="brand">Fjord Grace</div>
  </main>
</body>
</html>
```